Norwegian psychologist service needs a fresh and exiting web site*

Norwegian psychologist service: working with therapy, personal development, mastery and personal growth. Focus: children and teenagers with special needs; family dynamics; group processes; individuals with a need for therapy and personal growth. (Our company name: Fjordlys og samhold (means Mastery and Growth).

We already have a logo for the company, which will be used (will be attached in the project).

The webside is to be structured in 4 pages with roll down curtain menus (the numbers are just for guiding the designer - the should not be added):

Page 1: Om Fjordlys og Samhold (about Mastery and Growth): this is where our business is is presented/described shortly: Lorem Ipsum dolor cit...

Page 2: Tjenester (Services): this is where our 5 service areas are presented:
2.1 Utredning (Investigation, diagnosing): Lorem Ipsum dolor cit...
2.2 Rådgivning (consulting): Lorem Ipsum dolor cit...

2.3 Kurs og work shops (courses and work shops): Lorem Ipsum dolor cit...
2.3a Fjordlys og samhold Tema 1 (T1)
2.3b Fjordlys og samhold Tema 2 (T2)
2.3c Fjordlys og samhold Tema 3 (T3)

2.4 Terapi og utvikling (Therapy and development)
2.4a Fjordlys og samhold for individer (FS1)
2.4b Fjordlys og samhold i familier (FS2)
2.4c Fjordlys og samhold i grupper (FS3)
2.4d Fjordlys og samhold i institusjoner (FS4)

Page 3: Aktuelt (Blog): this is our blog where we share knowledge and articles

Page 4: Kontakt (Contact): This is the contact form page. Contact form should constitute:
- Ditt navn (your name)
- E-post (your e-mail)
- Emne (subject)
- Melding (message/description)

Our project should also include suggestion for handheld units (iPhone, iPad).
Updates

We have both been traveling with work for a while, and then unfortunately both of us got sick on return, so we need a few more days to evaluate and choose design. Kind Regards Arvid & Margit

Target Market(s)

Focus on therapy, learning, mastery and growth for children and teenagers with special needs, within the family dynamics, or in a group setting.
OUR MARKETS:
Private market: individuals, families, groups and health industry institutions (with focus on learning, mastery, growth (as well as growing up) and psychiatry for children and teenagers with special difficulties and needs)
Public institutions: Government institutions, state institutions and municipality institutions (e.g. schools, municipality health service, hospitals) that serve the public (families with children and teenagers with special needs, and where learning, mastery, growth (as well as growing up) and potential psychiatry is an issue).

Number of Pages Required

4 page

Font styles to use
Sans Serif

Colors

Designer to choose colors to be used in the design.

Requirements
Must have
• The website must have 4 pages with roll down curtain menus (we have added a PDF with suggested structure, and headings, with sub menus - see attached PDF drawing.
• The web page must also use the added logo file - and make the web page work well with our logo.
• We would like the website to have a modern look and we would like the site to be associated with typical HIGH END TOP QUALITY private health institutions, but with a stronger focus on human beings (hands, faces etc), and not white coats and doctors. We are psychologists in the private market.
• For instance, if photos are being used - we tend to like "warm" almost art-like, "grainy" two-tone (e.g. sepia) photos to illustrate our focus. If designer can find such photos as part of design, it would be interesting to us. We would like a few photos like that integrated in the design.
• We also want a design suggestion for how the web page should look like and behave on handheld units (e.g. iPhone, iPad).
Nice to have
• If designer could find a number of suitable photos that matches the business idea and design requirements (see description above), that could follow website, that would be good.
• It could also be nice to have graphic symbols that denote the different pages/subpages (subjects)....
• HORSES: we sometimes use horses as a "tool" in therapy sessions. The horse is not necessarily used for riding, but for contact, communication and grooming. PHOTOS: we would like the designer to find an opportunity for using a photo reflecting this cooperation between therapist, child, teenager and horse. It is a bit up to the designer to find a way to do this... Since the horse is only a tool, among many other tools, it does not have to be much - but we want to try and see how it will work with a photo that also reflects this part of our business.

```html
<!DOCTYPE html>
<html lang="no">
<head>
<meta charset="utf-8">
<title>Fjordlys og Samhold – Responsive Presentation</title>
<link rel="stylesheet" href="https://fonts.googleapis.com/css2?family=Roboto:wght@400;500;700&family=Source+Sans+3:wght@400&display=swap">
<style>
:root{
  --stage:#313944;
  --brand:#2b379c;
  --brand-deep:#222d86;
  --ink:#15172b;
  --muted:#3a3d52;
  --paper:#ffffff;
  --rule:#dcdde6;
  --hero-a:#b3a9cc;
  --hero-b:#8c8cc6;
  --hero-c:#6f76bd;
}
*{margin:0;padding:0;box-sizing:border-box}
html,body{width:1200px;height:2266px;overflow:hidden}
body{background:var(--stage);position:relative;font-family:"Roboto",Arial,sans-serif;color:var(--ink)}

.stage-title{position:absolute;left:0;width:1320px;text-align:center;color:var(--paper);font-family:"Source Sans 3",Arial,sans-serif;font-weight:400}
.stage-title.main{top:50px;font-size:36px}
.stage-title.sub{top:102px;font-size:21px}
.stage-label{position:absolute;color:var(--paper);font-family:"Source Sans 3",Arial,sans-serif;font-size:27px;text-align:center;width:300px;white-space:nowrap}
.stage-label.desktop{left:510px;top:748px;font-size:37px}
.stage-label.tablet{left:61px;top:855px}
.stage-label.mobile{left:915px;top:855px}

.screen{position:absolute;overflow:hidden;background:var(--paper)}
.screen.imac{left:207px;top:179px;width:576px;height:318px}
.screen.laptop{left:547px;top:356px;width:403px;height:253px}
.screen.phone{left:949px;top:431px;width:79px;height:190px}
.scaled{position:absolute;left:0;top:0;transform-origin:0 0}

/* ---------- desktop layout ---------- */
.site{position:relative;width:496px;height:1320px;background:var(--paper);overflow:hidden;font-family:"Roboto",Arial,sans-serif}
.site > *{position:absolute}
.topbar{left:0;top:0;width:496px;height:24px;background:var(--brand)}
.info{top:6px;display:flex;align-items:center;gap:3px;color:var(--paper);font-size:4.4px;line-height:1.25;font-weight:500}
.info svg{width:11px;height:11px}
.info b{display:block;font-weight:700}
.socials{top:6px;left:386px;display:flex;gap:2.5px}
.socials i{display:block;width:12px;height:12px;border-radius:50%;border:1.3px solid var(--paper)}
.hero{left:0;top:24px;width:496px;height:253px;
  background:
   radial-gradient(ellipse 90px 130px at 150px 110px,rgba(210,190,200,.55),transparent 70%),
   radial-gradient(ellipse 110px 140px at 390px 150px,rgba(120,120,190,.6),transparent 70%),
   linear-gradient(100deg,var(--hero-a) 0%,var(--hero-b) 48%,var(--hero-c) 100%)}
.logo{left:34px;top:30px;display:flex;align-items:center;gap:3px;color:var(--paper);font-size:6px;font-weight:500;letter-spacing:.4px}
.logo i{width:9px;height:9px;border-radius:50%;background:var(--paper);display:block}
.nav{top:37px;left:0;width:496px;height:8px}
.nav span{position:absolute;color:var(--paper);font-size:5.4px;font-weight:700;transform:translateX(-50%);white-space:nowrap}
.hero-title{left:0;top:101px;width:496px;text-align:center;color:var(--paper);font-size:17px;line-height:23px;font-weight:700}
.hero-copy{left:88px;top:154px;width:320px;text-align:center;color:var(--paper);font-size:5.6px;line-height:7.6px;font-weight:700}
.btn-light{left:209px;top:199px;width:79px;height:18px;border-radius:2px;background:var(--paper);color:var(--brand);font-size:5.6px;font-weight:700;display:flex;align-items:center;justify-content:center}
.section-title{left:0;width:496px;text-align:center;color:var(--brand);font-size:14.5px;font-weight:700}
.intro{left:128px;top:314px;width:240px;text-align:center;font-size:5.7px;line-height:7.4px;font-weight:700;color:var(--ink)}

.feature-img{width:212px;height:212px}
.img-family{left:248px;top:356px;
  background:radial-gradient(ellipse at 60% 45%,#8e93cf,transparent 70%),linear-gradient(160deg,#6c73b8,#4e58a6 60%,#6b6fb0);
  display:flex;align-items:center;justify-content:center;color:var(--paper);font-size:12px;font-weight:500}
.img-horse{left:36px;top:568px;
  background:radial-gradient(ellipse 70px 90px at 55% 45%,#f1ece8,transparent 75%),linear-gradient(180deg,#e8e2dc 0%,#d9cbbd 55%,#b8946c 100%)}
.img-paint{left:248px;top:780px;
  background:radial-gradient(ellipse 80px 70px at 40% 35%,#c9967b,transparent 75%),linear-gradient(170deg,#d8c6b4 0%,#b9927a 45%,#e9e4de 100%)}

.feature-text{width:196px}
.feature-text.left{left:36px}
.feature-text.right{left:268px;text-align:right}
.feature-text h3{font-size:15px;font-weight:700;color:var(--brand);line-height:18px}
.feature-text .bar{display:block;width:36px;height:1.4px;background:var(--brand);margin:3px 0 6px}
.feature-text.right .bar{margin-left:auto}
.feature-text .lead{font-size:5.5px;line-height:7px;font-weight:700;color:var(--brand);margin-bottom:6px}
.feature-text .body{font-size:5.5px;line-height:7px;font-weight:500;color:var(--ink)}
.btn-small{display:inline-block;margin-top:6px;padding:2.5px 4px;background:var(--brand);color:var(--paper);font-size:4.6px;font-weight:700;border-radius:2px}

.divider{left:0;top:1015px;width:496px;height:1px;background:var(--rule)}
.quote{left:130px;top:1056px;width:236px;text-align:center;font-size:5.6px;line-height:7.4px;color:var(--muted);font-weight:500}
.qmark{font-family:Georgia,serif;font-style:italic;font-weight:700;color:var(--brand);font-size:22px;line-height:1}
.avatar{border-radius:50%;background:radial-gradient(circle at 50% 40%,#d9d6d2,#8f8c8a 80%);border:1.5px solid #fff;box-shadow:0 0 0 .6px #999}
.person{left:0;top:1167px;width:496px;text-align:center;color:var(--brand);font-size:6.6px;font-weight:700}

.footer{left:0;top:1189px;width:496px;height:131px;background:var(--brand)}
.fcol{top:1202px;color:var(--paper)}
.fcol h4{font-size:6.2px;font-weight:700;margin-bottom:10px}
.fcol p{font-size:5.6px;font-weight:500;margin-bottom:9.5px;display:flex;align-items:center;gap:3px}
.fcol p i{display:block;width:6px;height:6px;border-radius:50%;background:var(--paper)}
.field{width:96px;height:10px;border:.7px solid var(--paper);border-radius:2px;font-size:4.3px;padding:2px 3px;position:relative;color:#c9cdf0}
.field svg{position:absolute;right:3px;top:1.5px;width:9px;height:6px}
.copyright{left:0;top:1303px;width:496px;text-align:center;color:var(--paper);font-size:5.4px;font-weight:500}

/* ---------- mobile layout ---------- */
.mobile-site{position:relative;width:162px;height:1738px;background:var(--paper);overflow:hidden;font-family:"Roboto",Arial,sans-serif}
.mobile-site > *{position:absolute}
.m-bar{left:0;top:0;width:162px;height:32px;background:var(--brand);display:flex;justify-content:center;align-items:center;gap:4px}
.m-bar i{display:block;width:13px;height:13px;border-radius:50%;border:1.4px solid var(--paper)}
.m-hero{left:0;top:32px;width:162px;height:308px;
  background:radial-gradient(ellipse 60px 90px at 110px 140px,rgba(120,120,190,.6),transparent 70%),linear-gradient(170deg,var(--hero-a),var(--hero-b) 50%,var(--hero-c))}
.m-logo{left:10px;top:42px;display:flex;align-items:center;gap:2px;color:var(--paper);font-size:5px;font-weight:500}
.m-logo i{display:block;width:7px;height:7px;border-radius:50%;background:var(--paper)}
.m-burger{left:138px;top:68px;width:12px;height:9px;border-top:1.5px solid #fff;border-bottom:1.5px solid #fff}
.m-burger::after{content:"";position:absolute;left:0;right:0;top:2.3px;height:1.5px;background:#fff}
.m-title{left:0;top:124px;width:162px;text-align:center;color:var(--paper);font-size:8.5px;line-height:11px;font-weight:700}
.m-copy{left:16px;top:152px;width:130px;text-align:center;color:var(--paper);font-size:5px;line-height:6.4px;font-weight:700}
.m-btn{left:61px;top:226px;width:40px;height:10px;background:var(--paper);color:var(--brand);font-size:3.8px;font-weight:700;border-radius:1.5px;display:flex;align-items:center;justify-content:center}
.m-h{left:0;width:162px;text-align:center;color:var(--brand);font-size:9px;font-weight:700}
.m-text{left:14px;width:134px;text-align:center;font-size:4.6px;line-height:5.9px;font-weight:500;color:var(--ink)}
.m-text .lead{color:var(--brand);font-weight:700;display:block}
.m-bar-rule{left:65px;width:32px;height:1px;background:var(--brand)}
.m-img{left:0;width:162px;height:162px}
.m-link{left:0;width:162px;text-align:center;font-size:3.8px;color:var(--brand);font-weight:700}
.m-divider{left:0;top:1419px;width:162px;height:1px;background:var(--rule)}
.m-avatars{left:0;top:1531px;width:162px;display:flex;justify-content:center;align-items:center;gap:3px}
.m-footer{left:0;top:1572px;width:162px;height:166px;background:var(--brand)}
.m-fitem{left:0;width:162px;text-align:center;color:var(--paper);font-size:5px;font-weight:700}
</style>
</head>
<body>

<svg width="0" height="0" style="position:absolute">
  <symbol id="ico-clock" viewBox="0 0 12 12"><circle cx="6" cy="6" r="5.2" fill="none" stroke="#fff" stroke-width="1"/><circle cx="6" cy="6" r="3.4" fill="none" stroke="#fff" stroke-width=".8"/><path d="M6 4v2.2l1.4 1" fill="none" stroke="#fff" stroke-width=".8"/></symbol>
  <symbol id="ico-mail" viewBox="0 0 12 12"><circle cx="6" cy="6" r="5.2" fill="none" stroke="#fff" stroke-width="1"/><rect x="3.3" y="4.2" width="5.4" height="3.8" fill="none" stroke="#fff" stroke-width=".7"/><path d="M3.3 4.2 6 6.4l2.7-2.2" fill="none" stroke="#fff" stroke-width=".7"/></symbol>
  <symbol id="ico-phone" viewBox="0 0 12 12"><circle cx="6" cy="6" r="5.6" fill="#fff"/><path d="M4.2 3.4c-.6.3-.8 1-.4 1.9.6 1.3 1.6 2.3 2.9 2.9.9.4 1.6.2 1.9-.4l-1.1-1-.7.5c-.7-.3-1.3-.9-1.6-1.6l.5-.7z" fill="#2b379c"/></symbol>
  <symbol id="ico-env" viewBox="0 0 9 6"><rect x=".4" y=".4" width="8.2" height="5.2" fill="none" stroke="#fff" stroke-width=".6"/><path d="M.4.4 4.5 3.3 8.6.4" fill="none" stroke="#fff" stroke-width=".6"/></symbol>
</svg>

<div class="stage-title main">Showcase Home Page</div>
<div class="stage-title sub">Responsive Presentation</div>

<!-- large screen -->
<div class="screen imac">
  <div class="site scaled" style="height:274px;transform:scale(1.1613)">
    <div class="topbar"></div>
    <div class="info" style="left:36px"><svg><use href="#ico-clock"/></svg><span><b>OUR SCHEDULE</b>8:00am - 5:00pm</span></div>
    <div class="info" style="left:140px"><svg><use href="#ico-mail"/></svg><span><b>EMAIL ADDRESS</b>Contact@fjordlysogsamhold.no</span></div>
    <div class="info" style="left:272px"><svg><use href="#ico-phone"/></svg><span><b>OUR PHONE NUMBER</b>555.201.4478</span></div>
    <div class="socials"><i></i><i></i><i></i><i></i><i></i></div>
    <div class="hero" role="img" aria-label="Photo: therapist seated in conversation with a young boy in a bright playroom, tinted blue-violet"></div>
    <div class="logo"><i></i>FJORDLYS</div>
    <div class="nav"><span style="left:260px">OM FJORDLYS OG SAMHOLD</span><span style="left:338px">TJENESTER</span><span style="left:393px">AKTUELT</span><span style="left:446px">KONTAKT</span></div>
    <div class="hero-title">WELCOM TO<br>FJORDLYS OG SAMHOLD</div>
    <div class="hero-copy">Lorem ipsum dolor sit amet, consetetur sadipscing elitr, sed diam nonumy eirmod tempor invidunt ut labore et dolore magna aliquyam erat, sed diam voluptua. At vero eos et accusam et justo duo dolores et ea rebum. Stet clita kasd gubergren, no sea takimata sanctus est Lorem ipsum dolor sit</div>
    <div class="btn-light">Learn More</div>
  </div>
</div>

<!-- laptop screen -->
<div class="screen laptop">
  <div class="site scaled" style="height:312px;transform:scale(.8125)">
    <div class="topbar"></div>
    <div class="info" style="left:36px"><svg><use href="#ico-clock"/></svg><span><b>OUR SCHEDULE</b>8:00am - 5:00pm</span></div>
    <div class="info" style="left:140px"><svg><use href="#ico-mail"/></svg><span><b>EMAIL ADDRESS</b>Contact@fjordlysogsamhold.no</span></div>
    <div class="info" style="left:272px"><svg><use href="#ico-phone"/></svg><span><b>OUR PHONE NUMBER</b>555.201.4478</span></div>
    <div class="socials"><i></i><i></i><i></i><i></i><i></i></div>
    <div class="hero" role="img" aria-label="Photo: therapist seated in conversation with a young boy in a bright playroom, tinted blue-violet"></div>
    <div class="logo"><i></i>FJORDLYS</div>
    <div class="nav"><span style="left:260px">OM FJORDLYS OG SAMHOLD</span><span style="left:338px">TJENESTER</span><span style="left:393px">AKTUELT</span><span style="left:446px">KONTAKT</span></div>
    <div class="hero-title">WELCOM TO<br>FJORDLYS OG SAMHOLD</div>
    <div class="hero-copy">Lorem ipsum dolor sit amet, consetetur sadipscing elitr, sed diam nonumy eirmod tempor invidunt ut labore et dolore magna aliquyam erat, sed diam voluptua. At vero eos et accusam et justo duo dolores et ea rebum. Stet clita kasd gubergren, no sea takimata sanctus est Lorem ipsum dolor sit</div>
    <div class="btn-light">Learn More</div>
    <div class="section-title" style="top:286px">What We Do?</div>
  </div>
</div>

<!-- phone screen -->
<div class="screen phone">
  <div class="mobile-site scaled" style="height:390px;transform:scale(.4877)">
    <div class="m-bar"><i></i><i></i><i></i><i></i><i></i></div>
    <div class="m-hero" role="img" aria-label="Photo: young boy in conversation with a therapist, tinted blue-violet"></div>
    <div class="m-logo"><i></i>FJORDLYS</div>
    <div class="m-burger"></div>
    <div class="m-title">WELCOM TO<br>FJORDLYS OG SAMHOLD</div>
    <div class="m-copy">Lorem ipsum dolor sit amet, consetetur sadipscing elitr, sed diam nonumy eirmod tempor invidunt ut labore et dolore magna aliquyam erat, sed diam voluptua. At vero eos et accusam et justo duo dolores et ea rebum. Stet clita kasd gubergren, no sea takimata sanctus est Lorem ipsum dolor sit</div>
    <div class="m-btn">Learn More</div>
  </div>
</div>

<div class="stage-label desktop">DESKTOP VERSION</div>
<div class="stage-label tablet">TABLET VERSION</div>
<div class="stage-label mobile">MOBILE VERSION</div>

<!-- desktop page -->
<div class="site" style="position:absolute;left:411px;top:840px">
  <div class="topbar"></div>
  <div class="info" style="left:36px"><svg><use href="#ico-clock"/></svg><span><b>OUR SCHEDULE</b>8:00am - 5:00pm</span></div>
  <div class="info" style="left:140px"><svg><use href="#ico-mail"/></svg><span><b>EMAIL ADDRESS</b>Contact@fjordlysogsamhold.no</span></div>
  <div class="info" style="left:272px"><svg><use href="#ico-phone"/></svg><span><b>OUR PHONE NUMBER</b>555.201.4478</span></div>
  <div class="socials"><i></i><i></i><i></i><i></i><i></i></div>
  <div class="hero" role="img" aria-label="Photo: therapist seated in conversation with a young boy in a bright playroom, tinted blue-violet"></div>
  <div class="logo"><i></i>FJORDLYS</div>
  <div class="nav"><span style="left:260px">OM FJORDLYS OG SAMHOLD</span><span style="left:338px">TJENESTER</span><span style="left:393px">AKTUELT</span><span style="left:446px">KONTAKT</span></div>
  <div class="hero-title">WELCOM TO<br>FJORDLYS OG SAMHOLD</div>
  <div class="hero-copy">Lorem ipsum dolor sit amet, consetetur sadipscing elitr, sed diam nonumy eirmod tempor invidunt ut labore et dolore magna aliquyam erat, sed diam voluptua. At vero eos et accusam et justo duo dolores et ea rebum. Stet clita kasd gubergren, no sea takimata sanctus est Lorem ipsum dolor sit</div>
  <div class="btn-light">Learn More</div>

  <div class="section-title" style="top:286px">What We Do?</div>
  <div class="intro">Lorem ipsum dolor sit amet, consetetur sadipscing elitr, sed diam nonumy eirmod tempor invidunt ut labore et dolore magna aliquyam erat, sed diam voluptua. At vero eos et accusam et justo duo dolores et ea rebum.</div>

  <div class="feature-img img-family" role="img" aria-label="Photo: smiling family sitting together on a sofa, tinted blue">Learn More</div>
  <div class="feature-img img-horse" role="img" aria-label="Photo: little girl playing with a wooden toy horse on the floor"></div>
  <div class="feature-img img-paint" role="img" aria-label="Photo: mother and son painting eggs at a table"></div>

  <div class="feature-text left" style="top:398px">
    <h3>Lorem Ipsum</h3><span class="bar"></span>
    <p class="lead">Lorem ipsum dolor sit amet, consetetur sadipscing elitr, sed diam nonumy eirmod tempor invidunt ut labore.</p>
    <p class="body">Et dolore magna aliquyam erat, sed diam voluptua. At vero eos et accusam et justo duo dolores et ea rebum. Stet clita kasd gubergren, no sea takimata sanctus est Lorem ipsum dolor sit amet. Lorem ipsum dolor sit amet, consetetur sadipscing elitr, sed diam nonumy eirmod tempor invidunt ut labore et dolore magna aliquyam erat, sed diam voluptua. At vero eos et accusam et justo duo dolores et ea rebum. Stet clita kasd gubergren, no sea takimata sanctus est Lorem ipsum dolor sit amet.</p>
    <span class="btn-small">Learn More ▸</span>
  </div>
  <div class="feature-text right" style="top:610px">
    <h3>Lorem Ipsum</h3><span class="bar"></span>
    <p class="lead">Lorem ipsum dolor sit amet, consetetur sadipscing elitr, sed diam nonumy eirmod tempor invidunt ut labore.</p>
    <p class="body">Et dolore magna aliquyam erat, sed diam voluptua. At vero eos et accusam et justo duo dolores et ea rebum. Stet clita kasd gubergren, no sea takimata sanctus est Lorem ipsum dolor sit amet. Lorem ipsum dolor sit amet, consetetur sadipscing elitr, sed diam nonumy eirmod tempor invidunt ut labore et dolore magna aliquyam erat, sed diam voluptua. At vero eos et accusam et justo duo dolores et ea rebum. Stet clita kasd gubergren, no sea takimata sanctus est Lorem ipsum dolor sit amet.</p>
    <span class="btn-small">Learn More ▸</span>
  </div>
  <div class="feature-text left" style="top:822px">
    <h3>Lorem Ipsum</h3><span class="bar"></span>
    <p class="lead">Lorem ipsum dolor sit amet, consetetur sadipscing elitr, sed diam nonumy eirmod tempor invidunt ut labore.</p>
    <p class="body">Et dolore magna aliquyam erat, sed diam voluptua. At vero eos et accusam et justo duo dolores et ea rebum. Stet clita kasd gubergren, no sea takimata sanctus est Lorem ipsum dolor sit amet. Lorem ipsum dolor sit amet, consetetur sadipscing elitr, sed diam nonumy eirmod tempor invidunt ut labore et dolore magna aliquyam erat, sed diam voluptua. At vero eos et accusam et justo duo dolores et ea rebum. Stet clita kasd gubergren, no sea takimata sanctus est Lorem ipsum dolor sit amet.</p>
    <span class="btn-small">Learn More ▸</span>
  </div>

  <div class="divider"></div>
  <div class="section-title" style="top:1031px;color:var(--ink);font-size:13px">Testimonials</div>
  <div class="qmark" style="left:116px;top:1048px">“</div>
  <div class="quote">Lorem ipsum dolor sit amet, consetetur sadipscing elitr, sed diam nonumy eirmod tempor invidunt ut labore et dolore magna aliquyam erat, sed diam voluptua. At vero eos et accusam et justo duo dolores et ea rebum. Stet clita kasd gubergren, no sea takimata sanctus est Lorem ipsum dolor sit amet. Lorem ipsum dolor sit amet, consetetur sadipscing elitr, sed diam</div>
  <div class="qmark" style="left:366px;top:1090px">”</div>
  <div class="avatar" role="img" aria-label="Client portrait" style="left:146px;top:1124px;width:32px;height:32px"></div>
  <div class="avatar" role="img" aria-label="Client portrait" style="left:183px;top:1124px;width:32px;height:32px"></div>
  <div class="avatar" role="img" aria-label="Client portrait of Jon Halvorsen" style="left:221px;top:1116px;width:48px;height:48px;background:radial-gradient(circle at 50% 40%,#6b5a50,#2a2220 80%)"></div>
  <div class="avatar" role="img" aria-label="Client portrait" style="left:274px;top:1124px;width:32px;height:32px"></div>
  <div class="avatar" role="img" aria-label="Client portrait" style="left:312px;top:1124px;width:32px;height:32px"></div>
  <div class="person">Jon Halvorsen</div>

  <div class="footer"></div>
  <div class="fcol" style="left:36px"><h4>COMPANY</h4><p>About</p><p>Terms and Polices</p><p>Guidelines</p></div>
  <div class="fcol" style="left:156px"><h4>SUPPORT</h4><p>Contact</p><p>Terms of us</p></div>
  <div class="fcol" style="left:256px"><h4>NEWSLETTER</h4><p>Join our monthly newsletter</p><div class="field">John@.........<svg><use href="#ico-env"/></svg></div></div>
  <div class="fcol" style="left:417px"><h4>Follow us</h4><p><i></i>Lysbok</p><p><i></i>Bildeflyt</p><p><i></i>Fagnett</p><p><i></i>Kvitter</p><p><i></i>Filmkanal</p></div>
  <div class="copyright">All rights reserved @FJORDLYS OG SAMHOLD</div>
</div>

<!-- tablet page -->
<div style="position:absolute;left:112px;top:946px;width:195px;height:519px;overflow:hidden">
<div class="site scaled" style="transform:scale(.3932)">
  <div class="topbar"></div>
  <div class="info" style="left:36px"><svg><use href="#ico-clock"/></svg><span><b>OUR SCHEDULE</b>8:00am - 5:00pm</span></div>
  <div class="info" style="left:140px"><svg><use href="#ico-mail"/></svg><span><b>EMAIL ADDRESS</b>Contact@fjordlysogsamhold.no</span></div>
  <div class="info" style="left:272px"><svg><use href="#ico-phone"/></svg><span><b>OUR PHONE NUMBER</b>555.201.4478</span></div>
  <div class="socials"><i></i><i></i><i></i><i></i><i></i></div>
  <div class="hero" role="img" aria-label="Photo: therapist seated in conversation with a young boy in a bright playroom, tinted blue-violet"></div>
  <div class="logo"><i></i>FJORDLYS</div>
  <div class="nav"><span style="left:260px">OM FJORDLYS OG SAMHOLD</span><span style="left:338px">TJENESTER</span><span style="left:393px">AKTUELT</span><span style="left:446px">KONTAKT</span></div>
  <div class="hero-title">WELCOM TO<br>FJORDLYS OG SAMHOLD</div>
  <div class="hero-copy">Lorem ipsum dolor sit amet, consetetur sadipscing elitr, sed diam nonumy eirmod tempor invidunt ut labore et dolore magna aliquyam erat, sed diam voluptua. At vero eos et accusam et justo duo dolores et ea rebum. Stet clita kasd gubergren, no sea takimata sanctus est Lorem ipsum dolor sit</div>
  <div class="btn-light">Learn More</div>
  <div class="section-title" style="top:286px">What We Do?</div>
  <div class="intro">Lorem ipsum dolor sit amet, consetetur sadipscing elitr, sed diam nonumy eirmod tempor invidunt ut labore et dolore magna aliquyam erat, sed diam voluptua. At vero eos et accusam et justo duo dolores et ea rebum.</div>
  <div class="feature-img img-family" role="img" aria-label="Photo: smiling family sitting together on a sofa, tinted blue">Learn More</div>
  <div class="feature-img img-horse" role="img" aria-label="Photo: little girl playing with a wooden toy horse on the floor"></div>
  <div class="feature-img img-paint" role="img" aria-label="Photo: mother and son painting eggs at a table"></div>
  <div class="feature-text left" style="top:398px">
    <h3>Lorem Ipsum</h3><span class="bar"></span>
    <p class="lead">Lorem ipsum dolor sit amet, consetetur sadipscing elitr, sed diam nonumy eirmod tempor invidunt ut labore.</p>
    <p class="body">Et dolore magna aliquyam erat, sed diam voluptua. At vero eos et accusam et justo duo dolores et ea rebum. Stet clita kasd gubergren, no sea takimata sanctus est Lorem ipsum dolor sit amet. Lorem ipsum dolor sit amet, consetetur sadipscing elitr, sed diam nonumy eirmod tempor invidunt ut labore et dolore magna aliquyam erat.</p>
    <span class="btn-small">Learn More ▸</span>
  </div>
  <div class="feature-text right" style="top:610px">
    <h3>Lorem Ipsum</h3><span class="bar"></span>
    <p class="lead">Lorem ipsum dolor sit amet, consetetur sadipscing elitr, sed diam nonumy eirmod tempor invidunt ut labore.</p>
    <p class="body">Et dolore magna aliquyam erat, sed diam voluptua. At vero eos et accusam et justo duo dolores et ea rebum. Stet clita kasd gubergren, no sea takimata sanctus est Lorem ipsum dolor sit amet. Lorem ipsum dolor sit amet, consetetur sadipscing elitr, sed diam nonumy eirmod tempor invidunt ut labore et dolore magna aliquyam erat.</p>
    <span class="btn-small">Learn More ▸</span>
  </div>
  <div class="feature-text left" style="top:822px">
    <h3>Lorem Ipsum</h3><span class="bar"></span>
    <p class="lead">Lorem ipsum dolor sit amet, consetetur sadipscing elitr, sed diam nonumy eirmod tempor invidunt ut labore.</p>
    <p class="body">Et dolore magna aliquyam erat, sed diam voluptua. At vero eos et accusam et justo duo dolores et ea rebum. Stet clita kasd gubergren, no sea takimata sanctus est Lorem ipsum dolor sit amet. Lorem ipsum dolor sit amet, consetetur sadipscing elitr, sed diam nonumy eirmod tempor invidunt ut labore et dolore magna aliquyam erat.</p>
    <span class="btn-small">Learn More ▸</span>
  </div>
  <div class="divider"></div>
  <div class="section-title" style="top:1031px;color:var(--ink);font-size:13px">Testimonials</div>
  <div class="qmark" style="left:116px;top:1048px">“</div>
  <div class="quote">Lorem ipsum dolor sit amet, consetetur sadipscing elitr, sed diam nonumy eirmod tempor invidunt ut labore et dolore magna aliquyam erat, sed diam voluptua. At vero eos et accusam et justo duo dolores et ea rebum. Stet clita kasd gubergren, no sea takimata sanctus est Lorem ipsum dolor sit amet.</div>
  <div class="qmark" style="left:366px;top:1090px">”</div>
  <div class="avatar" role="img" aria-label="Client portrait" style="left:146px;top:1124px;width:32px;height:32px"></div>
  <div class="avatar" role="img" aria-label="Client portrait" style="left:183px;top:1124px;width:32px;height:32px"></div>
  <div class="avatar" role="img" aria-label="Client portrait of Jon Halvorsen" style="left:221px;top:1116px;width:48px;height:48px;background:radial-gradient(circle at 50% 40%,#6b5a50,#2a2220 80%)"></div>
  <div class="avatar" role="img" aria-label="Client portrait" style="left:274px;top:1124px;width:32px;height:32px"></div>
  <div class="avatar" role="img" aria-label="Client portrait" style="left:312px;top:1124px;width:32px;height:32px"></div>
  <div class="person">Jon Halvorsen</div>
  <div class="footer"></div>
  <div class="fcol" style="left:36px"><h4>COMPANY</h4><p>About</p><p>Terms and Polices</p><p>Guidelines</p></div>
  <div class="fcol" style="left:156px"><h4>SUPPORT</h4><p>Contact</p><p>Terms of us</p></div>
  <div class="fcol" style="left:256px"><h4>NEWSLETTER</h4><p>Join our monthly newsletter</p><div class="field">John@.........<svg><use href="#ico-env"/></svg></div></div>
  <div class="fcol" style="left:417px"><h4>Follow us</h4><p><i></i>Lysbok</p><p><i></i>Bildeflyt</p><p><i></i>Fagnett</p><p><i></i>Kvitter</p><p><i></i>Filmkanal</p></div>
  <div class="copyright">All rights reserved @FJORDLYS OG SAMHOLD</div>
</div>
</div>

<!-- mobile page -->
<div style="position:absolute;left:1019px;top:948px;width:81px;height:869px;overflow:hidden">
<div class="mobile-site scaled" style="transform:scale(.5)">
  <div class="m-bar"><i></i><i></i><i></i><i></i><i></i></div>
  <div class="m-hero" role="img" aria-label="Photo: young boy in conversation with a therapist, tinted blue-violet"></div>
  <div class="m-logo"><i></i>FJORDLYS</div>
  <div class="m-burger"></div>
  <div class="m-title">WELCOM TO<br>FJORDLYS OG SAMHOLD</div>
  <div class="m-copy">Lorem ipsum dolor sit amet, consetetur sadipscing elitr, sed diam nonumy eirmod tempor invidunt ut labore et dolore magna aliquyam erat, sed diam voluptua. At vero eos et accusam et justo duo dolores et ea rebum. Stet clita kasd gubergren, no sea takimata sanctus est Lorem ipsum dolor sit</div>
  <div class="m-btn">Learn More</div>

  <div class="m-h" style="top:356px">What We Do?</div>
  <div class="m-text" style="top:380px">Lorem ipsum dolor sit amet, consetetur sadipscing elitr, sed diam nonumy eirmod tempor invidunt ut labore et dolore magna aliquyam erat, sed diam voluptua. At vero eos et accusam et justo duo dolores et ea rebum. Stet clita kasd gubergren, no sea takimata sanctus est.</div>

  <div class="m-img img-family" role="img" aria-label="Photo: smiling family sitting together on a sofa, tinted blue" style="top:449px;display:flex;align-items:center;justify-content:center;color:#fff;font-size:7px;font-weight:500">Learn More</div>
  <div class="m-h" style="top:618px">Lorem ipsum</div>
  <div class="m-bar-rule" style="top:632px"></div>
  <div class="m-text" style="top:640px"><span class="lead">Lorem ipsum dolor sit amet, consetetur sadipscing elitr.</span>Sed diam nonumy eirmod tempor invidunt ut labore et dolore magna aliquyam erat, sed diam voluptua. At vero eos et accusam et justo duo dolores et ea rebum. Stet clita kasd gubergren, no sea takimata sanctus est Lorem ipsum dolor sit amet. Lorem ipsum dolor sit amet, consetetur sadipscing elitr, sed diam nonumy eirmod tempor invidunt ut labore et dolore magna aliquyam erat.</div>
  <div class="m-link" style="top:754px">Learn More ▸</div>

  <div class="m-img img-horse" role="img" aria-label="Photo: little girl playing with a wooden toy horse on the floor" style="top:769px"></div>
  <div class="m-h" style="top:938px">Lorem ipsum</div>
  <div class="m-bar-rule" style="top:952px"></div>
  <div class="m-text" style="top:960px"><span class="lead">Lorem ipsum dolor sit amet, consetetur sadipscing elitr.</span>Sed diam nonumy eirmod tempor invidunt ut labore et dolore magna aliquyam erat, sed diam voluptua. At vero eos et accusam et justo duo dolores et ea rebum. Stet clita kasd gubergren, no sea takimata sanctus est Lorem ipsum dolor sit amet. Lorem ipsum dolor sit amet, consetetur sadipscing elitr, sed diam nonumy eirmod tempor invidunt ut labore et dolore magna aliquyam erat.</div>
  <div class="m-link" style="top:1076px">Learn More ▸</div>

  <div class="m-img img-paint" role="img" aria-label="Photo: mother and son painting eggs at a table" style="top:1091px"></div>
  <div class="m-h" style="top:1261px">Lorem ipsum</div>
  <div class="m-bar-rule" style="top:1275px"></div>
  <div class="m-text" style="top:1283px"><span class="lead">Lorem ipsum dolor sit amet, consetetur sadipscing elitr.</span>Sed diam nonumy eirmod tempor invidunt ut labore et dolore magna aliquyam erat, sed diam voluptua. At vero eos et accusam et justo duo dolores et ea rebum. Stet clita kasd gubergren, no sea takimata sanctus est Lorem ipsum dolor sit amet. Lorem ipsum dolor sit amet, consetetur sadipscing elitr, sed diam nonumy eirmod tempor invidunt ut labore et dolore magna aliquyam erat.</div>
  <div class="m-link" style="top:1400px">Learn More ▸</div>

  <div class="m-divider"></div>
  <div class="m-h" style="top:1430px;font-size:8px">Testimonials</div>
  <div class="qmark" style="left:6px;top:1448px;font-size:12px">“</div>
  <div class="m-text" style="top:1456px;color:var(--muted)">Invidunt ut labore et dolore magna aliquyam erat, sed diam voluptua. At vero eos et accusam et justo duo dolores et ea rebum. Stet clita kasd gubergren, no sea takimata sanctus est Lorem ipsum dolor sit amet, consetetur sadipscing elitr, sed diam nonumy eirmod tempor invidunt.</div>
  <div class="qmark" style="left:148px;top:1508px;font-size:12px">”</div>
  <div class="m-avatars">
    <div class="avatar" role="img" aria-label="Client portrait" style="width:14px;height:14px"></div>
    <div class="avatar" role="img" aria-label="Client portrait" style="width:14px;height:14px"></div>
    <div class="avatar" role="img" aria-label="Client portrait of Jon Halvorsen" style="width:21px;height:21px;background:radial-gradient(circle at 50% 40%,#6b5a50,#2a2220 80%)"></div>
    <div class="avatar" role="img" aria-label="Client portrait" style="width:14px;height:14px"></div>
    <div class="avatar" role="img" aria-label="Client portrait" style="width:14px;height:14px"></div>
  </div>
  <div class="m-link" style="top:1556px">Jon Halvorsen</div>

  <div class="m-footer"></div>
  <div class="m-fitem" style="top:1584px">COMPANY ▸</div>
  <div class="m-fitem" style="top:1617px">SUPPORT ▸</div>
  <div class="m-fitem" style="top:1650px">NEWSLETTER ▸</div>
  <div class="m-fitem" style="top:1683px">FOLLOW US ▸</div>
  <div class="m-fitem" style="top:1726px;font-size:4.2px;font-weight:500">All rights reserved @FJORDLYS OG SAMHOLD</div>
</div>
</div>

</body>
</html>
```